Poster Design for Film: 'Tres Lunas'

Tres Lunas means "two times" in Spanish. This short film is based on the true story of Cuban refugee during the take over of the Ordaz regime in 1959 and how is experiences and stories affected his children and grandchildren. Tres Lunas tells the story of Daniel- a recent grad who is forced to choose between his critically ill grandfather, the business opportunity of a lifetime, and maintaining a relationship with his love interest, Margaret. Through his grandfather's recollections as a young man in 1950's Cuba, Daniel gains a new outlook on life and the things that matter most.

This poster should evoke the drama and truth that the film approaches in a cinematic manner while maintaining the influences of true Cuban culture and history as perceived by a Miami audience today.

For more information please take a look at our fund raising site:
http://www.fundhaven.example/projects/tres-lunas

The grandfather's current life (the Cuban revolutionary/refugee as an old man):
www.clipvault.example/41592867
password: treslunas

A quick teaser of the film, exploring the lives of Daniel (the protagonist; grandson to Cuban refugee/revolutionary) and Meg (Daniel's love interest he neglects to commit to):

http://www.streamtube.example/watch?v=QbRtPwXnLeK

Please let me know if you would like any stills of the film, have any questions, etc. Thanks!

Hey all! So sorry for the delay on the stills- we had some serious technical issues, but now they are up!

Please let me know if you have any questions. We'll be uploaded more stills to choose from tonight.

Thanks!

Hey all!
Unless you need something in specific, I have just uploaded the final stills for the poster. Feel free to use any of the images, but please keep in mind that the main characters are Dan (the grandson), and his grandfather Arturo both young and old. In other words- the three guys.

Please let me know if you have any questions. Thanks! 

Here are some small text details for the bottom of the poster:

A Copper Lantern Production in association with BrightKiln Studios and the Coastal Pines University. Starring Brett Solano, Celina Fuentes, Omar Bustillo, Lucia Ortega, Farid Khoury. Written, Directed, & Produced by Marcos Ibarra. Director of Photography Tomas Varela. Edited by Marcos Ibarra & Tomas Varela.

Hey designers!

I've just uploaded a new still of the main character. Please try to include it in your design, as it is preferred over the other stills of the main character.

Thanks!

I've just uploaded two small logos to be featured on the bottom of the poster.

Thanks!

Target Market(s)

Hollywood. Cuban-Americans. Miamians. Film Critics. Students. Professors.

Adults based in Los Angeles and Miami aged 21-50 that speak English and Spanish and are in the art and entertainment industry.

Industry/Entity Type

Business

Requirements
Must have
• Must evoke the style of Cuba in the late 1950's while staying true to current day culture/style for 20-somethings in America (specifically LA, NYC, Miami).
Nice to have
• A sort of serious, almost stoic style that could possibly evoke a melancholic reaction.
Should not have
• Anything that evokes a daytime soap opera.

```html
<!DOCTYPE html>
<html lang="en">
<head>
<meta charset="utf-8">
<title>Tres Lunas — Film Poster</title>
<link rel="stylesheet" href="https://fonts.googleapis.com/css2?family=Architects+Daughter&display=swap">
<style>
  :root {
    --stone-black: #2b2a29;
    --stone-dark: #474442;
    --stone-mid: #6e6a66;
    --stone-light: #9d978f;
    --stone-pale: #b7b0a6;
    --ink-white: #f6f4f0;
    --shirt-white: #ece8e2;
    --skin-warm: #c39478;
    --skin-shadow: #9a6f58;
    --hair-dark: #1f1b19;
  }
  html, body {
    margin: 0;
    padding: 0;
    width: 800px;
    height: 1200px;
    overflow: hidden;
    background: var(--stone-dark);
  }
  .poster {
    position: relative;
    width: 800px;
    height: 1200px;
    overflow: hidden;
    font-family: "Architects Daughter", cursive;
    color: var(--ink-white);
  }
  .stone-backdrop {
    position: absolute;
    inset: 0;
    background:
      radial-gradient(circle at 78% 8%, var(--stone-black) 0%, transparent 16%),
      radial-gradient(circle at 92% 30%, var(--stone-black) 0%, transparent 14%),
      radial-gradient(circle at 55% 22%, var(--stone-dark) 0%, transparent 13%),
      radial-gradient(circle at 12% 6%, var(--stone-dark) 0%, transparent 12%),
      radial-gradient(circle at 40% 52%, var(--stone-dark) 0%, transparent 10%),
      radial-gradient(circle at 8% 70%, var(--stone-black) 0%, transparent 11%),
      radial-gradient(circle at 88% 66%, var(--stone-dark) 0%, transparent 12%),
      radial-gradient(circle at 22% 24%, var(--stone-pale) 0%, transparent 15%),
      radial-gradient(circle at 68% 44%, var(--stone-pale) 0%, transparent 14%),
      radial-gradient(circle at 30% 62%, var(--stone-light) 0%, transparent 16%),
      radial-gradient(circle at 60% 4%, var(--stone-light) 0%, transparent 12%),
      linear-gradient(165deg, var(--stone-mid) 0%, var(--stone-dark) 45%, var(--stone-mid) 75%, var(--stone-dark) 100%);
  }
  .lead-still {
    position: absolute;
    left: 0;
    top: 820px;
    width: 800px;
    height: 380px;
    background:
      radial-gradient(ellipse 17% 17% at 50% 14%, var(--hair-dark) 0%, var(--hair-dark) 55%, transparent 100%),
      radial-gradient(ellipse 14% 26% at 50% 42%, var(--skin-warm) 0%, var(--skin-shadow) 70%, transparent 100%),
      radial-gradient(ellipse 50% 12% at 15% 22%, var(--skin-warm) 0%, transparent 100%),
      radial-gradient(ellipse 50% 12% at 85% 22%, var(--skin-warm) 0%, transparent 100%),
      radial-gradient(ellipse 22% 22% at 6% 52%, var(--shirt-white) 0%, transparent 100%),
      radial-gradient(ellipse 22% 22% at 94% 52%, var(--shirt-white) 0%, transparent 100%),
      radial-gradient(ellipse 45% 40% at 50% 100%, var(--shirt-white) 0%, var(--shirt-white) 40%, transparent 100%),
      linear-gradient(180deg, transparent 0%, rgba(70,66,62,0.5) 30%, rgba(90,84,78,0.6) 100%);
  }
  .film-title {
    position: absolute;
    left: 0;
    width: 800px;
    top: 318px;
    margin: 0;
    text-align: center;
    font-size: 114px;
    font-weight: 400;
    letter-spacing: 1px;
    line-height: 1;
    white-space: nowrap;
  }
  .credit-label {
    position: absolute;
    left: 254px;
    top: 640px;
    margin: 0;
    font-size: 30px;
    line-height: 1;
    white-space: nowrap;
  }
  .director-name {
    position: absolute;
    left: 574px;
    top: 700px;
    margin: 0;
    font-size: 42px;
    line-height: 1.05;
    letter-spacing: 1px;
  }
</style>
</head>
<body>
  <main class="poster">
    <div class="stone-backdrop" role="img" aria-label="Weathered, mottled grey stone floor texture"></div>
    <div class="lead-still" role="img" aria-label="Still of the young lead lying on his back on the stone floor, hands behind his head, wearing a white t-shirt"></div>
    <h1 class="film-title">TRES LUNAS</h1>
    <p class="credit-label">written, directed and produced by</p>
    <p class="director-name">MARCOS<br>IBARRA</p>
  </main>
</body>
</html>
```